Kestrel Works Business Cards

This job is for the design of a business card.
I would like to review the design in 2x colour tones to choose from black and white inverted.
EG:
Black with white logo and white with black logo on BACK
White with black text on front and black with white text options
PRINTING DIMENSIONS: 4.5 x 8.5cm
Complete design will need to be provided in ready to print format with bleed lines
Target Market(s)
The audience of my business are people in the trade industry.
It will be also used for general networking with trades people and possible future clients.
I want to be represented as a professional, dynamic, creative and personable operator.
The card should reflect style, taste, experience, professionalism.
Industry/Entity Type
Business
Requirements
Must have
- BACK CONTENT:
- Logo in white and black background and vice versa with WHITE card and black logo review samples.
- FRONT CARD CONTENT:
- Name: Morgan Telvane
- Director
- Phone: 0438 216 947
- Email: morgan@kestrelworks.com.au
- Web: kestrelworks.com.au
- LICENCE #: KT-R 72158
Nice to have
- Possibly a textured background design on rear as a pose to a solid black
- Possibly adding a blue or orange discreet colour tone (possibly for email, phone abbreviated letter or symbols).

```html
<!DOCTYPE html>
<html lang="en">
<head>
<meta charset="utf-8">
<title>Kestrel Works Business Cards</title>
<link href="https://fonts.googleapis.com/css2?family=Roboto:wght@400;500&display=swap" rel="stylesheet">
<style>
  :root {
    --stage: #e0e0e0;
    --paper: #ffffff;
    --ink: #000000;
    --accent: #3fa9e0;
  }
  html, body {
    margin: 0;
    padding: 0;
    width: 1200px;
    height: 900px;
    overflow: hidden;
    background: var(--stage);
    font-family: "Roboto", Arial, sans-serif;
  }
  .sheet { position: relative; width: 1200px; height: 900px; }
  .card {
    position: absolute;
    width: 480px;
    height: 253px;
    box-sizing: border-box;
    overflow: hidden;
  }
  .card--light { background: var(--paper); color: var(--ink); }
  .card--dark { background: var(--ink); color: var(--paper); }
  .card--back-light { left: 106px; top: 182px; }
  .card--front-dark { left: 613px; top: 183px; }
  .card--front-light { left: 106px; top: 465px; height: 254px; }
  .card--back-dark { left: 613px; top: 466px; }

  .wordmark {
    position: absolute;
    font-weight: 500;
    text-transform: uppercase;
    white-space: nowrap;
    line-height: 1;
  }
  .card--back-light .wordmark,
  .card--back-dark .wordmark {
    left: 0; right: 0;
    text-align: center;
    font-size: 40px;
    letter-spacing: 1px;
  }
  .card--back-light .wordmark { top: 110px; }
  .card--back-dark .wordmark { top: 112px; }

  .card--front-dark .wordmark,
  .card--front-light .wordmark {
    right: 43px;
    top: 62px;
    font-size: 22px;
    letter-spacing: 0.5px;
  }

  .contact {
    position: absolute;
    right: 43px;
    top: 136px;
    text-align: right;
  }
  .contact__name {
    color: var(--accent);
    font-size: 13.5px;
    letter-spacing: 0.6px;
    text-transform: uppercase;
    line-height: 1;
  }
  .contact__role {
    font-size: 11px;
    margin-top: 2px;
    line-height: 1;
  }
  .contact__licence {
    font-size: 10px;
    margin-top: 3px;
    line-height: 1;
    letter-spacing: 0.3px;
  }
  .contact__list {
    list-style: none;
    margin: 11px 0 0;
    padding: 0;
  }
  .contact__item {
    display: flex;
    justify-content: flex-end;
    align-items: center;
    gap: 6px;
    font-size: 11px;
    height: 17px;
    letter-spacing: 0.3px;
    white-space: nowrap;
  }
  .contact__item strong { font-weight: 500; }
  .contact__icon {
    width: 12px;
    height: 12px;
    flex: none;
  }
</style>
</head>
<body>
<main class="sheet">

  <section class="card card--light card--back-light" aria-label="Card back, white">
    <div class="wordmark">Kestrel Works</div>
  </section>

  <section class="card card--dark card--front-dark" aria-label="Card front, black">
    <div class="wordmark">Kestrel Works</div>
    <div class="contact">
      <div class="contact__name">Morgan Telvane</div>
      <div class="contact__role">Director</div>
      <div class="contact__licence">Licence # KT-R 72158</div>
      <ul class="contact__list">
        <li class="contact__item"><span>0438 216 947</span>
          <svg class="contact__icon" viewBox="0 0 12 12"><circle cx="6" cy="6" r="5.4" fill="none" stroke="var(--accent)" stroke-width="0.9"/><path d="M4.4 3.4c-.6.4-.6 1.6.5 3s2.3 2.1 2.9 1.7l.4-.5-1-.8-.5.4c-.5-.2-1.2-.9-1.4-1.4l.4-.5-.8-1z" fill="var(--accent)"/></svg>
        </li>
        <li class="contact__item"><span>morgan@kestrelworks.com.au</span>
          <svg class="contact__icon" viewBox="0 0 12 12"><circle cx="6" cy="6" r="5.4" fill="none" stroke="var(--accent)" stroke-width="0.9"/><rect x="3.5" y="4.2" width="5" height="3.6" fill="var(--accent)"/><path d="M3.5 4.2 6 6.2 8.5 4.2" fill="none" stroke="#000" stroke-width="0.5"/></svg>
        </li>
        <li class="contact__item"><span>www.<strong>kestrelworks</strong>.com.au</span>
          <svg class="contact__icon" viewBox="0 0 12 12"><circle cx="6" cy="6" r="5.4" fill="none" stroke="var(--accent)" stroke-width="0.9"/><circle cx="4.2" cy="7.8" r="0.7" fill="var(--accent)"/><path d="M4 5.5a2.5 2.5 0 0 1 2.5 2.5M4 3.8a4.2 4.2 0 0 1 4.2 4.2" fill="none" stroke="var(--accent)" stroke-width="0.7"/></svg>
        </li>
      </ul>
    </div>
  </section>

  <section class="card card--light card--front-light" aria-label="Card front, white">
    <div class="wordmark">Kestrel Works</div>
    <div class="contact">
      <div class="contact__name">Morgan Telvane</div>
      <div class="contact__role">Director</div>
      <div class="contact__licence">Licence # KT-R 72158</div>
      <ul class="contact__list">
        <li class="contact__item"><span>0438 216 947</span>
          <svg class="contact__icon" viewBox="0 0 12 12"><circle cx="6" cy="6" r="5.4" fill="none" stroke="var(--accent)" stroke-width="0.9"/><path d="M4.4 3.4c-.6.4-.6 1.6.5 3s2.3 2.1 2.9 1.7l.4-.5-1-.8-.5.4c-.5-.2-1.2-.9-1.4-1.4l.4-.5-.8-1z" fill="var(--accent)"/></svg>
        </li>
        <li class="contact__item"><span>morgan@kestrelworks.com.au</span>
          <svg class="contact__icon" viewBox="0 0 12 12"><circle cx="6" cy="6" r="5.4" fill="none" stroke="var(--accent)" stroke-width="0.9"/><rect x="3.5" y="4.2" width="5" height="3.6" fill="var(--accent)"/><path d="M3.5 4.2 6 6.2 8.5 4.2" fill="none" stroke="#fff" stroke-width="0.5"/></svg>
        </li>
        <li class="contact__item"><span>www.<strong>kestrelworks</strong>.com.au</span>
          <svg class="contact__icon" viewBox="0 0 12 12"><circle cx="6" cy="6" r="5.4" fill="none" stroke="var(--accent)" stroke-width="0.9"/><circle cx="4.2" cy="7.8" r="0.7" fill="var(--accent)"/><path d="M4 5.5a2.5 2.5 0 0 1 2.5 2.5M4 3.8a4.2 4.2 0 0 1 4.2 4.2" fill="none" stroke="var(--accent)" stroke-width="0.7"/></svg>
        </li>
      </ul>
    </div>
  </section>

  <section class="card card--dark card--back-dark" aria-label="Card back, black">
    <div class="wordmark">Kestrel Works</div>
  </section>

</main>
</body>
</html>
```